Horse related business entrepreneur needs a business card

I need a business card design for my horse related business. The enterprise is Copper Vale LLC and I have 3 businesses (headquartered at 2 locations): 1. property management where we rent horse stalls and apartments at a thoroughbred training center outside Ocala; 2. a medium sized transportation service in central Florida that sells horse bedding and removes used horse bedding from horse farms; and horse racing

```html
<!DOCTYPE html>
<html lang="en">
<head>
<meta charset="utf-8">
<title>Copper Vale LLC — Business Card</title>
<link rel="stylesheet" href="https://fonts.googleapis.com/css2?family=Montserrat:wght@400;700;800&family=Open+Sans:wght@400;600&display=swap">
<style>
  :root {
    --backdrop: #3b3431;
    --card: #232323;
    --card-edge: #1a1a1a;
    --silver: #c9c9c9;
    --silver-soft: #a9a9a9;
    --muted: #7c7c7c;
  }
  * { box-sizing: border-box; margin: 0; padding: 0; }
  html, body {
    width: 1200px; height: 869px; overflow: hidden;
    background: var(--backdrop);
  }
  .stage {
    position: relative; width: 1200px; height: 869px;
    display: flex; align-items: center; justify-content: center; gap: 50px;
  }
  .card {
    position: relative; width: 520px; height: 297px;
    background: var(--card);
    border-radius: 6px;
    box-shadow: 0 0 0 1px var(--card-edge), 0 14px 30px rgba(0,0,0,.45);
    font-family: "Open Sans", sans-serif;
    color: var(--silver);
  }

  /* Front */
  .card-front {
    display: flex; flex-direction: column; align-items: center;
    padding-top: 40px;
  }
  .brand-mark {
    width: 96px; height: 96px; border-radius: 50%;
    background: var(--silver);
  }
  .brand-name {
    margin-top: 14px;
    font-family: "Montserrat", sans-serif; font-weight: 800;
    font-size: 30px; letter-spacing: 1px; color: var(--silver);
  }
  .addresses {
    margin-top: 12px; text-align: center;
    font-size: 13.5px; line-height: 1.55; color: var(--silver);
  }

  /* Back */
  .card-back { padding: 40px 0 0 40px; }
  .card-back .brand-name { margin-top: 0; font-size: 32px; }
  .person-name {
    margin-top: 14px;
    font-family: "Montserrat", sans-serif; font-weight: 700;
    font-size: 19px; color: var(--silver);
  }
  .person-role { font-size: 12px; color: var(--muted); margin-top: 1px; }
  .contact-list { list-style: none; margin-top: 16px; }
  .contact-list li {
    display: flex; align-items: center; gap: 12px;
    font-size: 14px; line-height: 19px; color: var(--silver);
  }
  .contact-list svg { width: 12px; height: 12px; flex: none; }
  .contact-list svg * { fill: none; stroke: var(--silver-soft); stroke-width: 1.4; }
</style>
</head>
<body>
<main class="stage">
  <section class="card card-front" aria-label="Card front">
    <div class="brand-mark" aria-hidden="true"></div>
    <h1 class="brand-name">COPPER VALE LLC</h1>
    <p class="addresses">
      1520 SE 90th Lane, Fairfield, FL 32634<br>
      718 Hollow Ridge Road, Ashby, VA 22950
    </p>
  </section>

  <section class="card card-back" aria-label="Card back">
    <h2 class="brand-name">COPPER VALE LLC</h2>
    <p class="person-name">Dana Whitlow</p>
    <p class="person-role">Owner</p>
    <ul class="contact-list">
      <li>
        <svg viewBox="0 0 12 12" aria-hidden="true"><path d="M3 1.5 L4.5 4 L3.5 5 Q5 7.5 7 8.5 L8 7.5 L10.5 9 L9.5 10.8 Q5 10.5 1.5 3 Z"/></svg>
        (555) 214-7730
      </li>
      <li>
        <svg viewBox="0 0 12 12" aria-hidden="true"><rect x="3" y="1.5" width="6" height="3"/><rect x="1.5" y="4.5" width="9" height="4.5"/><rect x="3" y="7.5" width="6" height="3"/></svg>
        (555) 214-7731
      </li>
      <li>
        <svg viewBox="0 0 12 12" aria-hidden="true"><rect x="1" y="2.5" width="10" height="7"/><path d="M1 2.5 L6 6.5 L11 2.5"/></svg>
        dana@coppervale.com
      </li>
      <li>
        <svg viewBox="0 0 12 12" aria-hidden="true"><circle cx="6" cy="6" r="4.8"/><ellipse cx="6" cy="6" rx="2" ry="4.8"/><path d="M1.2 6 H10.8"/></svg>
        www.coppervale.com
      </li>
    </ul>
  </section>
</main>
</body>
</html>
```